Family Owned Construction Company Needs Modern Business Cards

We need a new design for our business cards. We are a family owned construction company, Brantwell Construction, based in Mendon, Vermont and would like to add in our new logo and find a more modern look. We also want to use our old to make sure people know who we are. We do site development, highway, environmental, demolition, utility and aggregate.

Contact Information for Business Card

We want to have the office address, 418 Quarry Ridge Road, Ashbury Falls, AV 05788 and our phone (802) 555-0137 and fax (802) 555-0164 on there as well. Our website is www.brantwellinc.example. There should be a place for the person's name, title, cell number, and email address on the card. Words that we would like to be associated with our company are honesty, predictable, reliable, integrity, dedicated, built right quality, consistent, whatever it takes, and innovation. Safety is also very important to us.

Font styles to use
Serif
Sans Serif
Other font styles liked:
• Square 721 Extented

Colors
0255a3
ffffff

Requirements
Must have
• Office address, phone number and fax number. New logo with excavator
Nice to have
• That we do site development, highway, environmental, demolition, utility, and aggregate. Both logos

```html
<!DOCTYPE html>
<html lang="en">
<head>
<meta charset="utf-8">
<title>Brantwell Construction — Business Card</title>
<link href="https://fonts.googleapis.com/css2?family=Roboto+Condensed:wght@400;700&display=swap" rel="stylesheet">
<style>
  :root {
    --brand-blue: #0255a3;
    --brand-blue-deep: #013f7c;
    --paper: #ffffff;
    --paper-shade: #f1f3f6;
    --ink-muted: #5b6b80;
    --backdrop: #2a2421;
  }
  * { box-sizing: border-box; margin: 0; padding: 0; }
  html, body { width: 848px; height: 1200px; overflow: hidden; }
  body {
    background: var(--backdrop);
    font-family: "Roboto Condensed", Arial, sans-serif;
    display: flex;
    flex-direction: column;
    align-items: center;
    justify-content: center;
    gap: 90px;
  }
  .card {
    position: relative;
    width: 680px;
    height: 389px;
    border-radius: 4px;
    box-shadow: 0 14px 30px rgba(0,0,0,.45);
    overflow: hidden;
  }

  /* Front */
  .card-front {
    background: linear-gradient(135deg, #1a6cbb 0%, var(--brand-blue) 45%, var(--brand-blue-deep) 100%);
    color: var(--paper);
  }
  .wordmark {
    position: absolute;
    display: flex;
    align-items: center;
    gap: 18px;
  }
  .wordmark-mark {
    flex: none;
    background: currentColor;
  }
  .wordmark-name {
    font-weight: 700;
    text-transform: uppercase;
    line-height: 1;
  }
  .card-front .wordmark { left: 64px; top: 120px; }
  .card-front .wordmark-mark { width: 40px; height: 40px; }
  .card-front .wordmark-name { font-size: 52px; letter-spacing: 1px; }
  .card-front .wordmark-name span { display: block; font-size: 33px; letter-spacing: 6.5px; margin-top: 10px; }
  .front-web {
    position: absolute;
    right: 40px;
    bottom: 34px;
    font-size: 17px;
    font-weight: 700;
    letter-spacing: .5px;
  }

  /* Back */
  .card-back {
    background: linear-gradient(160deg, var(--paper) 0%, var(--paper-shade) 100%);
    color: var(--brand-blue);
  }
  .card-back::after {
    content: "";
    position: absolute;
    right: 0; top: 0; bottom: 0;
    width: 10px;
    background: var(--brand-blue);
  }
  .contact {
    position: absolute;
    left: 330px;
    top: 52px;
  }
  .contact-name { font-size: 30px; font-weight: 700; letter-spacing: 1px; text-transform: uppercase; }
  .contact-title { font-size: 12px; letter-spacing: 2px; text-transform: uppercase; color: var(--ink-muted); margin: 2px 0 18px; }
  .contact-list { list-style: none; font-size: 15px; color: var(--ink-muted); }
  .contact-list li { display: flex; align-items: center; gap: 10px; height: 24px; }
  .contact-list svg { width: 14px; height: 14px; flex: none; fill: none; stroke: var(--brand-blue); stroke-width: 1.6; }
  .contact-address { font-size: 15px; color: var(--ink-muted); line-height: 1.4; margin-top: 14px; }
  .contact-web { font-size: 15px; font-weight: 700; margin-top: 12px; }
  .card-back .wordmark { left: 40px; bottom: 48px; gap: 10px; }
  .card-back .wordmark-mark { width: 20px; height: 20px; }
  .card-back .wordmark-name { font-size: 26px; }
  .card-back .wordmark-name span { display: block; font-size: 16.5px; letter-spacing: 3.2px; margin-top: 6px; }
</style>
</head>
<body>

  <section class="card card-front" aria-label="Card front">
    <div class="wordmark">
      <div class="wordmark-mark"></div>
      <div class="wordmark-name">Brantwell<span>Construction Inc</span></div>
    </div>
    <p class="front-web">www.brantwellinc.example</p>
  </section>

  <section class="card card-back" aria-label="Card back">
    <div class="contact">
      <h1 class="contact-name">Alex Morgan</h1>
      <p class="contact-title">Director</p>
      <ul class="contact-list">
        <li>
          <svg viewBox="0 0 14 14"><rect x="2" y="2" width="10" height="10"/></svg>
          (802) 555-0137
        </li>
        <li>
          <svg viewBox="0 0 14 14"><path d="M3 1.5h2.5l1 3-1.5 1a7 7 0 0 0 3.5 3.5l1-1.5 3 1V11a1.5 1.5 0 0 1-1.5 1.5A10 10 0 0 1 1.5 3 1.5 1.5 0 0 1 3 1.5z"/></svg>
          (802) 555-0164
        </li>
        <li>
          <svg viewBox="0 0 14 14"><rect x="4" y="1" width="6" height="12" rx="1"/><line x1="6" y1="11" x2="8" y2="11"/></svg>
          +1 802 555 0199
        </li>
        <li>
          <svg viewBox="0 0 14 14"><rect x="1.5" y="3" width="11" height="8"/><path d="M1.5 3l5.5 4.5L12.5 3"/></svg>
          alex@brantwellinc.example
        </li>
      </ul>
      <p class="contact-address">418 Quarry Ridge Road<br>Ashbury Falls, AV 05788</p>
      <p class="contact-web">www.brantwellinc.example</p>
    </div>
    <div class="wordmark">
      <div class="wordmark-mark"></div>
      <div class="wordmark-name">Brantwell<span>Construction Inc</span></div>
    </div>
  </section>

</body>
</html>
```